Internet Of Things brochure

Need to create a brochure with a common theme to our website and the last 2 pages of the attached file. All the contect is in the file that I have attached.
website www.norvalenetworks.com.au

Industry/Entity Type

Internet

```html
<!DOCTYPE html>
<html lang="en">
<head>
<meta charset="utf-8">
<title>Norvale Networks Brochure Covers</title>
<link rel="stylesheet" href="https://fonts.googleapis.com/css2?family=Roboto+Condensed:wght@300;400;500;700&display=swap">
<style>
  :root {
    --stage: #ece7df;
    --paper: #ffffff;
    --paper-shade: #f1f1f3;
    --roof-grey: #ebe9ec;
    --brand-blue: #2f5597;
    --brand-blue-light: #5b86c6;
    --brand-blue-dark: #234483;
    --ink: #222222;
    --rule: #9a9a9a;
  }
  * { margin: 0; padding: 0; box-sizing: border-box; }
  html, body { width: 1200px; height: 1200px; overflow: hidden; background: var(--stage); }
  body { position: relative; font-family: "Roboto Condensed", sans-serif; }

  .page {
    position: absolute;
    top: 206px;
    width: 650px;
    height: 920px;
    transform: scale(0.857);
    transform-origin: top left;
    background: linear-gradient(160deg, var(--paper) 0%, var(--paper-shade) 100%);
    box-shadow: 0 4px 14px rgba(0,0,0,0.18);
    overflow: hidden;
  }
  .page--front { left: 31px; }
  .page--back { left: 614px; }
  .page svg.page-art { position: absolute; left: 0; top: 0; width: 650px; height: 920px; }

  .brand {
    position: absolute;
    display: flex;
    align-items: center;
    gap: 12px;
    color: var(--brand-blue);
    font-weight: 500;
    font-size: 44px;
    line-height: 1;
  }
  .brand__mark { width: 30px; height: 30px; background: var(--brand-blue); flex: none; }
  .brand__name { display: block; line-height: 1.02; }
  .page--front .brand { left: 68px; top: 72px; }
  .page--back .brand { left: 0; width: 650px; justify-content: center; top: 578px; }

  .headline { position: absolute; left: 226px; top: 296px; color: var(--ink); }
  .headline__lead { display: block; font-weight: 400; font-size: 40px; line-height: 1; }
  .headline__accent { display: block; font-weight: 400; font-size: 60px; line-height: 1; color: var(--brand-blue); margin-top: 8px; }
  .headline__strong { display: block; font-weight: 700; font-size: 44px; line-height: 1; margin-top: 8px; letter-spacing: 0.5px; }

  .footer-band {
    position: absolute; left: 0; bottom: 0; width: 650px; height: 38px;
    background: var(--brand-blue);
    border-top: 3px solid #ffffff;
    box-shadow: 0 -3px 0 var(--brand-blue-light);
    color: #ffffff; font-size: 15px; letter-spacing: 2px;
    display: flex; align-items: center; justify-content: center;
  }

  .contact-box {
    position: absolute; left: 66px; top: 758px; width: 516px; height: 74px;
    border: 1.5px solid var(--rule); border-radius: 8px;
  }
  .contact-box__title {
    position: absolute; left: 50%; top: -10px; transform: translateX(-50%);
    background: #f8f8f9; padding: 0 10px;
    color: var(--brand-blue); font-weight: 700; font-size: 15px; line-height: 18px; letter-spacing: 0.5px;
  }
  .contact-item { position: absolute; display: flex; gap: 7px; font-size: 11.5px; line-height: 14px; color: var(--ink); }
  .contact-item svg { flex: none; width: 18px; height: 18px; margin-top: 1px; }
  .contact-item strong { display: block; color: var(--brand-blue-dark); font-weight: 700; }
  .contact-item--head { left: 50px; top: 16px; }
  .contact-item--sales { left: 208px; top: 16px; }
  .contact-item--phone { left: 346px; top: 18px; align-items: center; }
  .contact-item--mail { left: 346px; top: 40px; align-items: center; }
</style>
</head>
<body>

<section class="page page--front">
  <svg class="page-art" viewBox="0 0 650 920">
    <defs>
      <linearGradient id="teamTone" x1="0" y1="0" x2="0" y2="1">
        <stop offset="0" stop-color="#e8e6ea"/>
        <stop offset="0.35" stop-color="#b9a9a0"/>
        <stop offset="0.7" stop-color="#4a4a55"/>
        <stop offset="1" stop-color="#1f2027"/>
      </linearGradient>
    </defs>
    <polygon points="0,405 412,165 650,300 650,920 0,920" fill="var(--roof-grey)"/>
    <polygon points="0,355 412,103 650,238 650,292 412,155 0,397" fill="var(--brand-blue)"/>
    <polygon points="0,355 412,103 650,238 650,252 412,118 0,370" fill="var(--brand-blue-light)" opacity="0.5"/>
    <rect x="0" y="430" width="650" height="452" fill="url(#teamTone)" role="img" aria-label="Photo of five smiling IT professionals in business attire"/>
  </svg>

  <div class="brand"><span class="brand__mark"></span><span class="brand__name">Norvale<br>Networks</span></div>

  <h1 class="headline">
    <span class="headline__lead">A growing organisation</span>
    <span class="headline__accent">of experienced</span>
    <span class="headline__strong">IT PROFESSIONALS</span>
  </h1>

  <div class="footer-band">www.norvalenetworks.com.au</div>
</section>

<section class="page page--back">
  <svg class="page-art" viewBox="0 0 650 920">
    <defs>
      <linearGradient id="meetingTone" x1="0" y1="0" x2="1" y2="1">
        <stop offset="0" stop-color="#d9c2b2"/>
        <stop offset="0.4" stop-color="#e9edf1"/>
        <stop offset="0.75" stop-color="#3a3f4c"/>
        <stop offset="1" stop-color="#1d2230"/>
      </linearGradient>
    </defs>
    <polygon points="0,255 325,440 650,245 650,292 325,497 0,305" fill="var(--brand-blue)"/>
    <polygon points="0,262 325,450 650,252 650,266 325,464 0,276" fill="var(--brand-blue-light)" opacity="0.5"/>
    <polygon points="0,0 650,0 650,245 325,432 0,255" fill="url(#meetingTone)" role="img" aria-label="Photo of three colleagues in a business meeting reviewing charts at a table"/>
  </svg>

  <div class="brand"><span class="brand__mark"></span><span class="brand__name">Norvale<br>Networks</span></div>

  <div class="contact-box">
    <div class="contact-box__title">CONTACT US</div>
    <div class="contact-item contact-item--head">
      <svg viewBox="0 0 18 18"><circle cx="9" cy="9" r="9" fill="var(--brand-blue)"/><path d="M4 9.2 9 5l5 4.2h-1.6V13H10.4v-2.6H7.6V13H5.6V9.2z" fill="#fff"/></svg>
      <div><strong>Granville Head Office</strong>118-120 Meridian Road<br>Granville, NSW, 2142</div>
    </div>
    <div class="contact-item contact-item--sales">
      <svg viewBox="0 0 18 18"><circle cx="9" cy="9" r="9" fill="var(--brand-blue)"/><path d="M4 9.2 9 5l5 4.2h-1.6V13H10.4v-2.6H7.6V13H5.6V9.2z" fill="#fff"/></svg>
      <div><strong>Sales Office</strong>14 Ashford Lane<br>Sydney NSW 2000</div>
    </div>
    <div class="contact-item contact-item--phone">
      <svg viewBox="0 0 18 18"><circle cx="9" cy="9" r="9" fill="var(--brand-blue)"/><path d="M6.2 4.6l1.6 1.8-.9 1.3c.6 1.3 1.6 2.3 2.9 2.9l1.3-.9 1.8 1.6-.9 1.7C9 13 5 9 4.5 5.5z" fill="#fff"/></svg>
      <div>1300 555 019</div>
    </div>
    <div class="contact-item contact-item--mail">
      <svg viewBox="0 0 18 18"><circle cx="9" cy="9" r="9" fill="var(--brand-blue)"/><rect x="4.5" y="6" width="9" height="6.5" fill="#fff"/><path d="M4.5 6 9 9.6 13.5 6" fill="none" stroke="var(--brand-blue)" stroke-width="1"/></svg>
      <div>info@norvalenet.com.au</div>
    </div>
  </div>

  <div class="footer-band">www.norvalenetworks.com.au</div>
</section>

</body>
</html>
```